Morvex Business Card (intended for Business Card sized magnet)

Hi guys,

I would like to get a design for my business card for the restaurant. The design must be single sided as I intend to produce business card sized magnets.

The File attached must me on and I'm open for new ides

Can you please ensure that the design meets Cardowell's magnetic business card size specifications:

http://www.cardowell.example.au/custom-magnets.aspx?txi=15695&xnid=TopNav_Magnetic+Business+Cards+(linked+item)_Magnets_Marketing+Products&xnav=TopNav

Full Bleed Size (starting document size):
90 x 52 mm
1062 x 615 pixels
* Finished artwork should use the full bleed dimensions for best results.

Document Trim Size (final size after being cut):
87 x 49 mm
1028 x 579 pixels
* Please be sure to keep all text within the safe margin.

Resolution:
300 DPI

The winning design/source files need to meet these specifications.

Thanks
Updates

Hi guys, can I see more options please Thanks

```html
<!DOCTYPE html>
<html lang="en">
<head>
<meta charset="utf-8">
<title>Morvex Business Card</title>
<link rel="stylesheet" href="https://fonts.googleapis.com/css2?family=PT+Sans+Narrow:wght@400;700&display=swap">
<style>
  :root {
    --card-top: #232425;
    --card-mid: #1d1e1f;
    --card-low: #0d0e0e;
    --panel-top: #3b4446;
    --panel-bottom: #151819;
    --logo-paper: #ffffff;
    --ink: #111111;
    --type-light: #eeeeee;
    --rule: #d4d4d4;
  }
  html, body {
    margin: 0;
    padding: 0;
    width: 693px;
    height: 1200px;
    overflow: hidden;
    background: var(--card-low);
  }
  .card {
    position: relative;
    width: 693px;
    height: 1200px;
    overflow: hidden;
    background: linear-gradient(180deg, var(--card-top) 0%, var(--card-mid) 55%, var(--card-low) 73%);
    font-family: "PT Sans Narrow", "Arial Narrow", sans-serif;
  }
  .logo-plate {
    position: absolute;
    left: 43px;
    top: 150px;
    width: 613px;
    height: 361px;
    background: var(--logo-paper);
    display: flex;
    align-items: center;
    justify-content: center;
  }
  .brand-name {
    margin: 0;
    font-family: "PT Sans Narrow", "Arial Narrow", sans-serif;
    font-weight: 400;
    font-size: 150px;
    line-height: 1;
    color: var(--ink);
    letter-spacing: 2px;
  }
  .phone-line {
    position: absolute;
    left: 126px;
    top: 592px;
    width: 450px;
    height: 92px;
  }
  .phone-icon {
    position: absolute;
    left: 0;
    top: 6px;
    width: 50px;
    height: 70px;
  }
  .phone-number {
    position: absolute;
    left: 82px;
    top: -2px;
    margin: 0;
    font-size: 76px;
    font-weight: 400;
    line-height: 1;
    color: var(--type-light);
    letter-spacing: 0.5px;
    white-space: nowrap;
  }
  .phone-rule {
    position: absolute;
    left: 60px;
    top: 87px;
    width: 384px;
    height: 3px;
    background: var(--rule);
  }
  .contact-panel {
    position: absolute;
    left: 0;
    top: 875px;
    width: 693px;
    height: 325px;
    background: linear-gradient(180deg, var(--panel-top) 0%, #262c2e 45%, var(--panel-bottom) 100%);
    color: var(--type-light);
    text-align: center;
  }
  .contact-item {
    position: absolute;
    left: 0;
    width: 100%;
    margin: 0;
    font-size: 42px;
    line-height: 1;
    white-space: nowrap;
  }
  .contact-address { top: 26px; }
  .contact-email { top: 134px; }
  .contact-web { top: 245px; }
</style>
</head>
<body>
  <main class="card">
    <div class="logo-plate">
      <h1 class="brand-name">Morvex</h1>
    </div>

    <div class="phone-line">
      <svg class="phone-icon" viewBox="0 0 50 70" aria-hidden="true">
        <path d="M14 4 L22 2 L27 20 L20 24 C19 34 22 44 28 52 L35 48 L45 62 L38 67 C24 70 8 50 4 30 C2 18 6 8 14 4 Z" fill="var(--type-light)"/>
      </svg>
      <p class="phone-number">03 9418 2750</p>
      <div class="phone-rule"></div>
    </div>

    <section class="contact-panel">
      <p class="contact-item contact-address">214 Larkfield Rd, Ashcombe South, 3170</p>
      <p class="contact-item contact-email">morvex214@inbox.example</p>
      <p class="contact-item contact-web">www.morvex.example.au</p>
    </section>
  </main>
</body>
</html>
```